International Medical Company Needs a Website Design for a Support Site

We need a website design for a support site we are doing for ostomates called Bright Rebounds. We are an international company but this website is for our Australian market.

The website is a support site for people who are living with an Ostomy or Bowel Disease. This is a site where they can read other ostomates' stories and how they are dealing with the fact that they have to wear a pouch everyday.

The URL for our US site is: http://www.brightrebounds-example.com/

We need to use the same logo but we have freedom around the color scheme. We are not fond of the brown color scheme used in our US site and are happy for designs to be submitted with alternatives.

• We want the design to be clean, inspiring, modern and inviting.
• We would like to see a design for the mainpage / homepage and one of the subpages
• We only require the PSD / image files (no HTML needed)

Attached to this project is our sitemap, an example wireframe and the logos. We are happy for you to play around with different options and don't have to stick to the layout shown in the wireframe.

If you have any further questions please ask.

```html
<!DOCTYPE html>
<html lang="en">
<head>
<meta charset="utf-8">
<title>Bright Rebounds</title>
<link href="https://fonts.googleapis.com/css2?family=Lato:ital,wght@0,400;0,700;1,400&display=swap" rel="stylesheet">
<style>
:root{
  --brown:#9a6130;
  --brown-dark:#7d4c22;
  --ink:#222;
  --text:#444;
  --rule:#8a8a8a;
  --white:#fff;
  --grey-btn:#c4c4c4;
  --dark-btn:#333;
}
*{box-sizing:border-box;margin:0;padding:0}
html,body{width:1200px;height:1004px;overflow:hidden;background:var(--white);font-family:'Lato',sans-serif;color:var(--text)}
.page{position:relative;width:1200px;height:1004px;overflow:hidden}
a{color:inherit;text-decoration:none}

.site-header{position:absolute;left:0;top:0;width:1200px;height:133px;background:var(--white);box-shadow:0 2px 4px rgba(0,0,0,.18);z-index:2}
.brand{position:absolute;left:152px;top:50px;display:flex;align-items:center;gap:8px}
.brand-mark{width:18px;height:18px;border-radius:50%;background:var(--brown)}
.brand-name{font-size:17px;font-weight:700;letter-spacing:1px;color:var(--brown);text-transform:uppercase}
.pill{display:inline-flex;align-items:center;gap:8px;background:var(--brown);color:var(--white);border-radius:8px;font-size:11.5px;font-weight:700;box-shadow:0 1px 2px rgba(0,0,0,.3)}
.pill svg{width:8px;height:10px}
.share-top{position:absolute;left:581px;top:23px;height:28px;padding:0 12px 0 11px}
.country-label{position:absolute;left:765px;top:32px;font-size:11.5px;color:var(--brown)}
.country-select{position:absolute;left:896px;top:27px;width:152px;height:24px;border:1px solid #ddd;background:#fbf8f5;font-size:11.5px;padding:6px 14px;color:#555}
.country-select svg{position:absolute;right:14px;top:8px;width:10px;height:7px}
.main-nav{position:absolute;left:391px;top:77px;display:flex;align-items:center;font-size:13.5px;color:var(--ink)}
.main-nav a{margin-right:26px}
.main-nav .current{color:var(--brown);border:1px solid var(--brown);border-radius:8px;padding:6px 15px;margin-right:33px}
.search-icon{position:absolute;left:1033px;top:83px;width:15px;height:15px}

.hero{position:absolute;left:0;top:133px;width:1200px;height:429px;background:var(--white);border-bottom:1px solid #bbb}
.hero-photo{position:absolute;left:291px;top:0;width:909px;height:429px;background:linear-gradient(90deg,rgba(255,255,255,1) 0%,rgba(240,232,226,.7) 18%,#eadfd6 40%,#dcd0c7 55%,#f2ece8 75%,#c7d3b9 100%)}
.hero-fade{position:absolute;left:291px;top:0;width:200px;height:429px;background:linear-gradient(90deg,#fff,rgba(255,255,255,0))}
.hero-title{position:absolute;left:152px;top:150px;font-size:29px;font-weight:700;color:var(--ink)}
.hero-sub{position:absolute;left:152px;top:198px;width:330px;font-size:15px;line-height:23px;color:var(--brown)}
.hero-actions{position:absolute;left:153px;top:298px;display:flex;align-items:center;gap:14px}
.btn-block{display:flex;align-items:center;height:37px;font-size:11.5px}
.btn-block span{padding:0 13px 0 11px}
.btn-block i{display:flex;align-items:center;justify-content:center;width:40px;height:37px;border-left:1px solid rgba(255,255,255,.4)}
.btn-dark{background:var(--dark-btn);color:var(--white)}
.btn-grey{background:var(--grey-btn);color:var(--ink);border:1px solid #aaa}
.btn-grey i{border-left-color:#999}
.or{font-size:19px;color:var(--ink)}

.column{position:absolute;top:604px;width:286px}
.column h2{font-size:19.5px;font-weight:400;color:#111;padding-bottom:12px;border-bottom:1px solid var(--rule)}
.column p{font-size:11.3px;line-height:19px;color:var(--text);margin-top:12px}
.column p+p{margin-top:19px}
.about{left:153px}
.share{left:457px}
.news{left:762px}
.read-more{position:absolute;top:235px;height:28px;padding:0 14px 0 11px}
.news-list{list-style:none;margin-top:14px}
.news-item{position:relative;height:86px}
.news-thumb{position:absolute;left:0;top:0;width:76px;height:57px;background:linear-gradient(135deg,#3a2a22 0%,#b0673a 45%,#efe9e3 75%)}
.news-title{position:absolute;left:86px;top:1px;font-size:13px;font-weight:700;color:var(--brown)}
.news-text{position:absolute;left:86px;top:19px;width:200px;font-size:10.8px;line-height:17px;font-style:italic;color:var(--text)}
.news-date{position:absolute;left:0;top:66px;font-size:10.5px;font-style:italic;color:var(--ink)}

.site-footer{position:absolute;left:0;top:956px;width:1200px;height:48px;background:var(--brown)}
.footer-links{position:absolute;right:152px;top:17px;display:flex;gap:22px;font-size:11.5px;font-weight:700;color:var(--white)}
</style>
</head>
<body>
<div class="page">
  <header class="site-header">
    <a class="brand" href="#"><span class="brand-mark"></span><span class="brand-name">Bright Rebounds</span></a>
    <a class="pill share-top" href="#">Share Your Story <svg viewBox="0 0 8 10"><path d="M2 1l4 4-4 4" fill="none" stroke="#fff" stroke-width="1.6"/></svg></a>
    <span class="country-label">Choose Your Country:</span>
    <div class="country-select">Australia <svg viewBox="0 0 10 7"><path d="M1 1l4 4 4-4" fill="none" stroke="#999" stroke-width="1.3"/></svg></div>
    <nav class="main-nav">
      <a class="current" href="#">Home</a>
      <a href="#">About Us</a>
      <a href="#">Personal Stories</a>
      <a href="#">Tips for Living</a>
      <a href="#">News</a>
      <a href="#">Resources</a>
      <a href="#">Contact Us</a>
    </nav>
    <svg class="search-icon" viewBox="0 0 15 15"><circle cx="6" cy="6" r="4.3" fill="none" stroke="#222" stroke-width="2"/><path d="M9 9l5 5" stroke="#222" stroke-width="2.4"/></svg>
  </header>

  <section class="hero">
    <div class="hero-photo" role="img" aria-label="Photo of a doctor listening to a young female patient in a bright clinic"></div>
    <div class="hero-fade"></div>
    <h1 class="hero-title">Sharing Stories and Giving Hope</h1>
    <p class="hero-sub">to the people around the world who are facing inflammatory bowel disease, colorectal cancer, or have had ostomy surgery.</p>
    <div class="hero-actions">
      <a class="btn-block btn-dark" href="#"><span>Share a Story</span><i><svg width="17" height="17" viewBox="0 0 17 17"><circle cx="13" cy="3.5" r="2.6" fill="#ccc"/><circle cx="4" cy="8.5" r="2.6" fill="#ccc"/><circle cx="13" cy="13.5" r="2.6" fill="#ccc"/><path d="M13 3.5L4 8.5l9 5" fill="none" stroke="#ccc" stroke-width="1.5"/></svg></i></a>
      <span class="or">or</span>
      <a class="btn-block btn-grey" href="#"><span>Read Stories</span><i><svg width="18" height="17" viewBox="0 0 18 17"><path d="M11 5V1H1v15h10v-4" fill="none" stroke="#666" stroke-width="1.6"/><path d="M6 8.5h10M13 5.5l3 3-3 3" fill="none" stroke="#666" stroke-width="1.6"/></svg></i></a>
    </div>
  </section>

  <section class="column about">
    <h2>What is Bright Rebounds</h2>
    <p>Lorem Ipsum is simply dummy text of the printing and typesetting industry. Lorem Ipsum has been the industry's standard dummy text ever since the 1500, when an unknown printer took a galley of type and scrambled it to make a type specimen book.</p>
    <p>t has survived not only five centuries, but also the leap into electronic typesetting, remaining essentially</p>
    <a class="pill read-more" href="#">Read more <svg viewBox="0 0 8 10"><path d="M2 1l4 4-4 4" fill="none" stroke="#fff" stroke-width="1.6"/></svg></a>
  </section>

  <section class="column share">
    <h2>Share a Story</h2>
    <p>It is a long established fact that a reader will be distracted by the readable content of a page when looking at its layout.</p>
    <p>The point of using Lorem Ipsum is that it has a more-or-less normal distribution of letters, as opposed to using Content here. content of a page when look at its layout.</p>
    <a class="pill read-more" href="#">Read more <svg viewBox="0 0 8 10"><path d="M2 1l4 4-4 4" fill="none" stroke="#fff" stroke-width="1.6"/></svg></a>
  </section>

  <section class="column news">
    <h2>News</h2>
    <ul class="news-list">
      <li class="news-item"><div class="news-thumb" role="img" aria-label="Photo of a person writing at a desk"></div><a class="news-title" href="#">Chunk of Lorem Ipsum</a><p class="news-text">There are many variations of passages of Lorem Ipsum available...</p><span class="news-date">31-Mar-14</span></li>
      <li class="news-item"><div class="news-thumb" role="img" aria-label="Photo of a person writing at a desk"></div><a class="news-title" href="#">Standard of Lorem Ipsum</a><p class="news-text">There are many variations of passages of Lorem Ipsum available...</p><span class="news-date">30-Mar-14</span></li>
      <li class="news-item"><div class="news-thumb" role="img" aria-label="Photo of a person writing at a desk"></div><a class="news-title" href="#">The Chunks Lorem Ipsum</a><p class="news-text">There are many variations of passages of Lorem Ipsum available...</p><span class="news-date">28-Mar-14</span></li>
    </ul>
  </section>

  <footer class="site-footer">
    <nav class="footer-links"><a href="#">Legal Notice</a><a href="#">Privacy Policy</a><a href="#">Sitemap</a></nav>
  </footer>
</div>
</body>
</html>
```